Corporate Design für Facharztpraxis
Zielgruppe
Es handelt sich um eine Allgemeinmedizin Praxis mit dem Zusatzschwerpunkt Proktologie(Diagnostik und Therapie von Enddarmerkrankungen).Ansonsten wird das komplette Spektrum der Allg.med.abgedeckt.
Aufgabenstellung
Moderenes Logo, welches knapp und prägnant sowohl den Allgemeinärztliche teil, als auch den prokrotologischen Teil abbildet. Farblich dezent herausgestellt.

```html
<!DOCTYPE html>
<html lang="de">
<head>
<meta charset="utf-8">
<title>Hausarztpraxis Jonas Berger – Geschäftsausstattung</title>
<link rel="stylesheet" href="https://fonts.googleapis.com/css2?family=Montserrat:wght@400;500;600;700&family=Roboto:wght@400;500&display=swap">
<style>
  :root {
    --green: #8dc63f;
    --green-light: #b4da7e;
    --blue: #17577a;
    --grey: #d1d2d4;
    --grey-dark: #a7a9ac;
    --text-soft: #8a8c8f;
    --paper: #ffffff;
    --stage: #f1f1ef;
  }
  * { box-sizing: border-box; margin: 0; padding: 0; }
  html, body { width: 1200px; height: 1200px; overflow: hidden; background: var(--stage); }
  body { position: relative; font-family: "Montserrat", sans-serif; color: var(--blue); }

  .sheet { position: absolute; background: var(--paper); overflow: hidden; }
  .sheet.is-green { background: var(--green); }
  .item-label { position: absolute; font-family: "Roboto", sans-serif; font-size: 7px; color: #333; }

  /* brand lockup: plain circle + name */
  .brand { position: absolute; display: flex; align-items: center; gap: 6px; }
  .brand-dot { flex: none; border-radius: 50%; background: var(--blue); }
  .brand-name { font-family: "Montserrat", sans-serif; font-weight: 500; line-height: 1.05; color: var(--blue); }
  .is-green .brand-name { color: #fff; }

  /* letterhead */
  .letterhead { left: 219px; top: 102px; width: 356px; height: 504px; }
  .fold-mark { position: absolute; left: 0; width: 13px; height: 1px; background: #bbb; }
  .letter-footer { position: absolute; left: 12px; top: 457px; display: flex; font-family: "Roboto", sans-serif; font-size: 3.6px; color: var(--text-soft); line-height: 1.6; }
  .letter-footer .col { padding: 0 14px 0 0; margin-right: 14px; border-right: 0.6px solid #ccc; }
  .letter-footer .col:last-child { border: 0; }
  .letter-footer h4 { font-size: 3.6px; font-weight: 500; margin-bottom: 3px; }
  .letter-bar { position: absolute; left: 0; bottom: 0; width: 293px; height: 8px; background: var(--blue); }

  /* logo banners */
  .banner { left: 626px; width: 365px; height: 179px; }

  /* envelopes */
  .envelope { left: 617px; width: 374px; height: 188px; }
  .env-bar { position: absolute; left: 0; bottom: 0; width: 241px; height: 10px; background: var(--blue); }
  .env-url { position: absolute; font-size: 8px; letter-spacing: 2px; }
  .env-window { position: absolute; left: 35px; top: 83px; width: 169px; height: 74px; border-radius: 4px; background: var(--grey); }

  /* business cards */
  .card { width: 146px; height: 94px; }
  .card-name { position: absolute; font-family: "Roboto", sans-serif; font-weight: 500; color: var(--blue); }
  .contact { position: absolute; font-family: "Roboto", sans-serif; font-size: 4.6px; line-height: 1.35; color: var(--blue); }
  .contact li { list-style: none; display: flex; align-items: center; gap: 3px; }
  .contact svg { width: 4px; height: 4px; flex: none; }
  .card-url { position: absolute; font-size: 5px; letter-spacing: 1px; }
</style>
</head>
<body>

<!-- Briefbogen -->
<section class="sheet letterhead">
  <div class="brand" style="left:12px;top:14px;">
    <span class="brand-dot" style="width:40px;height:40px;"></span>
    <span class="brand-name" style="font-size:15px;">Hausarztpraxis<br>Jonas Berger</span>
  </div>
  <span class="fold-mark" style="top:178px"></span>
  <span class="fold-mark" style="top:252px"></span>
  <span class="fold-mark" style="top:355px"></span>
  <div class="letter-footer">
    <div class="col">
      <h4>HAUSARZTPRAXIS JONAS BERGER</h4>
      XXXXX Str. 26<br>00000 Germany<br>USt-ID-Nr DE 000 000 000
    </div>
    <div class="col">
      <h4>KONTAKT</h4>
      +49 0000 00000 0<br>+49 0000 00000 00<br>info@jonas-berger.de<br>www.jonas-berger.de
    </div>
    <div class="col">
      <h4>BANKVERBINDUNG</h4>
      XXXXXXXXXXX<br>IBAN DE 00 0000 0000 0000 0000 00<br>BIC XXXXXXXXXX
    </div>
  </div>
  <span class="letter-bar"></span>
</section>

<!-- Logo auf Grün / auf Weiß -->
<section class="sheet banner is-green" style="top:123px;">
  <div class="brand" style="left:46px;top:50px;gap:12px;">
    <span class="brand-dot" style="width:78px;height:78px;"></span>
    <span class="brand-name" style="font-size:26px;">Hausarztpraxis<br>Jonas Berger</span>
  </div>
</section>
<section class="sheet banner" style="top:308px;">
  <div class="brand" style="left:46px;top:50px;gap:12px;">
    <span class="brand-dot" style="width:78px;height:78px;"></span>
    <span class="brand-name" style="font-size:26px;">Hausarztpraxis<br>Jonas Berger</span>
  </div>
</section>

<!-- Umschläge -->
<span class="item-label" style="left:604px;top:522px;">1</span>
<section class="sheet envelope" style="top:520px;">
  <div class="brand" style="left:11px;top:8px;">
    <span class="brand-dot" style="width:44px;height:44px;"></span>
    <span class="brand-name" style="font-size:14px;">Hausarztpraxis<br>Jonas Berger</span>
  </div>
  <span class="env-bar"></span>
  <span class="env-url" style="right:12px;bottom:1px;">www.jonas-berger.de</span>
</section>

<span class="item-label" style="left:604px;top:738px;">1</span>
<section class="sheet envelope" style="top:736px;">
  <div class="brand" style="left:11px;top:8px;">
    <span class="brand-dot" style="width:44px;height:44px;"></span>
    <span class="brand-name" style="font-size:14px;">Hausarztpraxis<br>Jonas Berger</span>
  </div>
  <span class="env-window"></span>
  <span class="brand-dot" style="position:absolute;left:264px;top:84px;width:48px;height:48px;background:var(--grey-dark);"></span>
  <span class="env-url" style="left:235px;top:150px;color:var(--grey-dark);">www.jonas-berger.de</span>
</section>

<span class="item-label" style="left:604px;top:952px;">1</span>
<section class="sheet envelope is-green" style="top:950px;">
  <span class="brand-dot" style="position:absolute;left:190px;top:25px;width:150px;height:150px;background:var(--green-light);"></span>
  <div class="brand" style="left:9px;top:12px;">
    <span class="brand-dot" style="width:46px;height:46px;"></span>
    <span class="brand-name" style="font-size:15px;">Hausarztpraxis<br>Jonas Berger</span>
  </div>
  <span class="env-window"></span>
  <span class="env-url" style="left:91px;top:164px;color:#e4f1d2;">www.jonas-berger.de</span>
</section>

<!-- Visitenkarten, Vorderseiten -->
<span class="item-label" style="left:217px;top:641px;">1</span>
<section class="sheet card" style="left:236px;top:639px;">
  <div class="brand" style="left:11px;top:31px;gap:5px;">
    <span class="brand-dot" style="width:32px;height:32px;"></span>
    <span class="brand-name" style="font-size:11px;">Hausarztpraxis<br>Jonas Berger</span>
  </div>
</section>

<span class="item-label" style="left:217px;top:754px;">2</span>
<section class="sheet card" style="left:236px;top:752px;">
  <span class="brand-dot" style="position:absolute;left:-10px;top:2px;width:104px;height:104px;"></span>
  <span class="card-url" style="right:6px;bottom:6px;">www.jonas-berger.de</span>
</section>

<span class="item-label" style="left:217px;top:864px;">3</span>
<section class="sheet card is-green" style="left:236px;top:862px;">
  <div class="brand" style="left:11px;top:31px;gap:5px;">
    <span class="brand-dot" style="width:32px;height:32px;"></span>
    <span class="brand-name" style="font-size:11px;">Hausarztpraxis<br>Jonas Berger</span>
  </div>
</section>

<!-- Visitenkarten, Rückseiten -->
<span class="item-label" style="left:408px;top:641px;">A</span>
<section class="sheet card" style="left:425px;top:639px;">
  <div class="brand" style="left:10px;top:5px;gap:5px;">
    <span class="brand-dot" style="width:30px;height:30px;"></span>
    <span class="brand-name" style="font-size:11px;">Hausarztpraxis Jonas Berger</span>
  </div>
  <span class="card-name" style="left:8px;top:58px;font-size:8.5px;">Jonas Berger</span>
  <ul class="contact" style="left:75px;top:42px;">
    <li><svg viewBox="0 0 4 4"><circle cx="2" cy="1.6" r="1.3" fill="none" stroke="currentColor" stroke-width=".6"/><path d="M2 4 L1 2.4 H3Z" fill="currentColor"/></svg>XXXXXXXstr. 1</li>
    <li style="padding-left:7px;margin-bottom:3px;">00000 Germany</li>
    <li><svg viewBox="0 0 4 4"><rect x=".3" y="1" width="3.4" height="2.6" rx=".5" fill="currentColor"/></svg>+49 0000 - 000 00 0</li>
    <li><svg viewBox="0 0 4 4"><rect x=".3" y="1" width="3.4" height="2.6" rx=".5" fill="currentColor"/></svg>+49 0000 - 000 00 00</li>
    <li><svg viewBox="0 0 4 4"><rect x="1.1" y=".2" width="1.8" height="3.6" rx=".3" fill="currentColor"/></svg>+49 000 - 000 00 00</li>
    <li><svg viewBox="0 0 4 4"><rect x=".2" y=".8" width="3.6" height="2.4" fill="currentColor"/></svg>info@jonas-berger.de</li>
    <li><svg viewBox="0 0 4 4"><circle cx="2" cy="2" r="1.7" fill="none" stroke="currentColor" stroke-width=".5"/></svg>www.jonas-berger.de</li>
  </ul>
</section>

<span class="item-label" style="left:408px;top:754px;">B</span>
<section class="sheet card is-green" style="left:422px;top:752px;">
  <div class="brand" style="left:5px;top:5px;gap:5px;">
    <span class="brand-dot" style="width:28px;height:28px;"></span>
    <span class="brand-name" style="font-size:12px;">Hausarztpraxis Jonas Berger</span>
  </div>
  <span class="card-name" style="left:42px;top:40px;font-size:10px;">Jonas Berger</span>
  <ul class="contact" style="left:12px;top:61px;">
    <li><svg viewBox="0 0 4 4"><circle cx="2" cy="1.6" r="1.3" fill="none" stroke="currentColor" stroke-width=".6"/><path d="M2 4 L1 2.4 H3Z" fill="currentColor"/></svg>XXXXXXXstr. 1</li>
    <li style="padding-left:7px;">00000 Germany</li>
  </ul>
  <ul class="contact" style="left:80px;top:61px;">
    <li><svg viewBox="0 0 4 4"><rect x=".3" y="1" width="3.4" height="2.6" rx=".5" fill="currentColor"/></svg>+49 0000 - 000 00 0</li>
    <li><svg viewBox="0 0 4 4"><rect x=".3" y="1" width="3.4" height="2.6" rx=".5" fill="currentColor"/></svg>+49 0000 - 000 00 00</li>
    <li><svg viewBox="0 0 4 4"><rect x="1.1" y=".2" width="1.8" height="3.6" rx=".3" fill="currentColor"/></svg>+49 000 - 000 00 00</li>
    <li><svg viewBox="0 0 4 4"><rect x=".2" y=".8" width="3.6" height="2.4" fill="currentColor"/></svg>info@jonas-berger.de</li>
    <li><svg viewBox="0 0 4 4"><circle cx="2" cy="2" r="1.7" fill="none" stroke="currentColor" stroke-width=".5"/></svg>www.jonas-berger.de</li>
  </ul>
</section>

<span class="item-label" style="left:408px;top:864px;">C</span>
<section class="sheet card" style="left:425px;top:862px;">
  <span class="brand-dot" style="position:absolute;left:-10px;top:16px;width:76px;height:76px;"></span>
  <span class="card-name" style="right:6px;top:6px;font-size:11px;font-family:'Montserrat',sans-serif;">Jonas Berger</span>
  <ul class="contact" style="left:79px;top:41px;">
    <li><svg viewBox="0 0 4 4"><circle cx="2" cy="1.6" r="1.3" fill="none" stroke="currentColor" stroke-width=".6"/><path d="M2 4 L1 2.4 H3Z" fill="currentColor"/></svg>XXXXXXXstr. 1</li>
    <li style="padding-left:7px;margin-bottom:3px;">00000 Germany</li>
    <li><svg viewBox="0 0 4 4"><rect x=".3" y="1" width="3.4" height="2.6" rx=".5" fill="currentColor"/></svg>+49 0000 - 000 00 0</li>
    <li><svg viewBox="0 0 4 4"><rect x=".3" y="1" width="3.4" height="2.6" rx=".5" fill="currentColor"/></svg>+49 0000 - 000 00 00</li>
    <li><svg viewBox="0 0 4 4"><rect x="1.1" y=".2" width="1.8" height="3.6" rx=".3" fill="currentColor"/></svg>+49 000 - 000 00 00</li>
    <li><svg viewBox="0 0 4 4"><rect x=".2" y=".8" width="3.6" height="2.4" fill="currentColor"/></svg>info@jonas-berger.de</li>
    <li><svg viewBox="0 0 4 4"><circle cx="2" cy="2" r="1.7" fill="none" stroke="currentColor" stroke-width=".5"/></svg>www.jonas-berger.de</li>
  </ul>
</section>

</body>
</html>
```